New audiology website PSD design only - guaranteed

We need a clean and attractive website to replace an existing Audiology (hearing technology) website which will be wordpress based.
The current website is: http://pelmorahearing.com.au
They have a new logo and colors which you can find at www.quodel.net/temp/plh2018.pdf
We will no longer have a web shop in the new website
To enter the competition, we only need a sample of the home page.
The winning design will be asked to produce 2 standard page template alternatives as well (based on the winning home page design, but for a standard page layout)
The winning design must provide any photos used
We want a clean, credible site but with some warmth
Target Market(s)
All ages but needs to include the elderly
Industry/Entity Type
Medical And Science
Number of Pages Required
3 page
Look and feel
Each slider illustrates characteristics of the customer's brand and the style your logo design should communicate.

```html
<!DOCTYPE html>
<html lang="en">
<head>
<meta charset="utf-8">
<title>Pelmora Hearing – Home</title>
<link href="https://fonts.googleapis.com/css2?family=Playfair+Display:wght@400;700&family=Open+Sans:wght@400;600;700&display=swap" rel="stylesheet">
<style>
:root{
  --orange:#f26522;
  --dark:#2b2b2b;
  --ink:#333;
  --muted:#666;
  --grey-band:#f1f1f1;
  --line:#e2e2e2;
  --white:#fff;
  --stage:#f3f3f3;
  --hero-tone:linear-gradient(100deg,#cdb8a6 0%,#c89a74 28%,#e7b58c 52%,#c79a7c 72%,#8a7a72 100%);
  --clinic-tone:linear-gradient(170deg,#eef1f3 0%,#cfd6dc 38%,#7d8795 68%,#2f3747 100%);
  --exam-tone:linear-gradient(160deg,#9aa1a9 0%,#5b6170 45%,#262b36 100%);
  --iem-clear:linear-gradient(160deg,#7b7f86 0%,#4a4e56 45%,#24272d 100%);
  --iem-blue:linear-gradient(160deg,#dfe6ef 0%,#8fa6cf 35%,#3557a6 60%,#c6cfdc 100%);
  --map-tone:linear-gradient(135deg,#eeede8 0%,#e4ecdc 30%,#f1ebd8 55%,#e8e7e2 100%);
  --serif:'Playfair Display', Georgia, serif;
  --sans:'Open Sans', Arial, sans-serif;
}
*{box-sizing:border-box;margin:0;padding:0}
html,body{width:1200px;height:3468px;overflow:hidden}
body{background:var(--stage);font-family:var(--sans);color:var(--ink);position:relative}
ul{list-style:none}
.btn{display:inline-block;background:var(--orange);color:var(--white);font:700 8px var(--sans);letter-spacing:.5px;text-transform:uppercase;padding:7px 16px}
.photo{box-shadow:inset 0 0 40px rgba(0,0,0,.08)}

/* ---------- Desktop ---------- */
.desktop{position:absolute;left:16px;top:65px;width:823px;background:var(--white);box-shadow:0 4px 20px rgba(0,0,0,.12)}
.topbar{height:23px;background:var(--dark);color:#ddd;font-size:8px;display:flex;justify-content:space-between;align-items:center;padding:0 88px}
.topbar span{display:flex;align-items:center;gap:5px}
.mainnav{height:46px;display:flex;align-items:center;padding:0 88px;justify-content:space-between;border-bottom:1px solid var(--line)}
.brand{display:flex;align-items:center;gap:7px;font:600 18px var(--sans);color:var(--ink)}
.brand-dot{width:18px;height:18px;border-radius:50%;background:var(--orange)}
.menu{display:flex;gap:20px;font-size:8.5px;font-weight:600;color:var(--ink)}
.menu .active{color:var(--orange);border-bottom:2px solid var(--orange);padding-bottom:4px}
.hero{position:relative;height:393px;background:var(--hero-tone)}
.hero-lines{position:absolute;left:72px;top:118px;font:400 34px/1.3 var(--serif);color:var(--white);text-shadow:0 1px 6px rgba(0,0,0,.15)}
.hero-lines span{display:block}
.hero-lines span:nth-child(2){margin-left:50px}
.hero-lines span:nth-child(3){margin-left:110px}
.hero-arrow{position:absolute;top:206px;width:14px;height:14px;border-radius:50%;background:rgba(255,255,255,.85)}
.hero-arrow svg{display:block}
.service-card{position:absolute;left:527px;top:229px;width:202px;height:180px;background:var(--white);box-shadow:0 6px 18px rgba(0,0,0,.15);text-align:center;padding:36px 20px 0}
.service-card h2{font:700 17px/1.3 var(--serif);color:var(--ink);margin-bottom:18px}
.aids{position:relative;height:386px}
.aids-photo{position:absolute;left:88px;top:47px;width:215px;height:200px;background:var(--clinic-tone)}
.aids-photo.inset{left:150px;top:150px;width:170px;height:155px;background:var(--exam-tone);box-shadow:0 2px 8px rgba(0,0,0,.25)}
.aids-copy{position:absolute;left:388px;top:100px;width:350px}
h2.section{font:700 20px var(--serif);color:var(--ink)}
.copy{font-size:7.5px;line-height:15px;color:var(--muted)}
.aids-copy .copy{margin:10px 0 14px}
.musicians{position:relative;height:400px;background:var(--grey-band);text-align:center}
.musicians h2.section{padding-top:38px}
.m-card{position:absolute;top:83px;width:300px;height:256px;background:var(--white);box-shadow:0 2px 8px rgba(0,0,0,.08)}
.m-card .photo{height:142px}
.m-card .tag{position:absolute;right:0;top:0;width:26px;height:26px;background:var(--orange);display:flex;align-items:center;justify-content:center}
.m-card h3{font:700 7.5px var(--sans);margin:18px 0 6px;text-transform:uppercase}
.m-card .copy{padding:0 40px;line-height:12px}
.m-card .btn{position:absolute;left:50%;bottom:-12px;transform:translateX(-50%)}
.side-arrow{position:absolute;top:205px;width:20px;height:20px;border-radius:50%;border:1px solid #999;background:var(--white)}
.about{position:relative;height:356px;border-bottom:1px solid var(--line)}
.about h2.section{position:absolute;left:320px;top:52px}
.about .copy{position:absolute;left:88px;top:105px;width:335px;line-height:14px}
.about .btn{position:absolute;left:320px;top:275px}
.about-photo{position:absolute;left:515px;top:45px;width:215px;height:270px;background:var(--clinic-tone)}
.location{height:157px;text-align:center;padding-top:30px}
.locs{display:flex;justify-content:center;margin-top:22px}
.loc{width:250px;font-size:7.5px;line-height:13px;color:var(--ink)}
.loc strong{display:block;font-size:8px;margin-bottom:4px}
.loc+.loc{border-left:1px solid var(--line)}
.map{height:335px;background:var(--map-tone)}
.footer{background:var(--dark);color:#ccc;height:365px;position:relative;font-size:7px}
.fcol{position:absolute}
.fcol h4{font:700 7.5px var(--sans);color:var(--white);text-transform:uppercase;margin-bottom:14px}
.fcol li{display:flex;align-items:center;gap:8px;margin-bottom:10px}
.ico{width:14px;height:14px;border-radius:50%;border:1px solid #aaa;flex:none}
.subscribe{display:flex;width:170px;height:22px;background:var(--white);margin-top:8px;align-items:center;justify-content:space-between;padding:0 8px;color:#999}
.links{display:grid;grid-template-columns:1fr 1fr;column-gap:40px;row-gap:4px;width:250px}
.copyright{position:absolute;left:88px;right:88px;bottom:48px;border-top:1px solid #444;padding-top:12px;text-align:center;font-size:6.5px;color:#aaa}

/* ---------- Mobile ---------- */
.mobile{position:absolute;left:897px;top:153px;width:259px;background:var(--white);box-shadow:0 4px 20px rgba(0,0,0,.12)}
.mobile .topbar{height:22px;padding:0 60px;font-size:6px;justify-content:flex-start}
.m-nav{height:52px;display:flex;align-items:center;justify-content:space-between;padding:0 14px}
.m-nav .brand{font-size:13px;gap:5px}
.m-nav .brand-dot{width:13px;height:13px}
.m-nav .toggle{font:700 7px var(--sans);display:flex;align-items:center;gap:4px}
.m-hero{position:relative;height:305px;background:var(--hero-tone)}
.m-hero .hero-lines{left:10px;top:20px;font-size:24px}
.m-hero .hero-lines span:nth-child(2){margin-left:45px}
.m-hero .hero-lines span:nth-child(3){margin-left:110px}
.m-hero .service-card{left:80px;top:170px;width:150px;height:128px;padding:22px 10px 0}
.m-hero .service-card h2{font-size:14px;margin-bottom:10px}
.m-hero .service-card .btn{font-size:6px;padding:5px 10px}
.m-aids{height:624px;padding:64px 14px 0}
.m-aids .photo{height:294px;margin:0 12px 24px;background:var(--exam-tone)}
.m-aids h2.section{font-size:17px;margin-bottom:8px}
.m-aids .copy,.m-about .copy{font-size:6px;line-height:11.5px}
.m-aids .btn,.m-about .btn{margin-top:14px;font-size:6px;padding:6px 12px}
.m-musicians{height:601px;background:var(--grey-band);padding:40px 14px 0;text-align:center}
.m-musicians h2.section{font-size:16px;margin-bottom:22px}
.m-musicians .m-card{position:relative;top:0;width:220px;height:220px;margin:0 auto 36px}
.m-musicians .m-card .photo{height:132px}
.m-musicians .m-card .tag{width:20px;height:20px}
.m-musicians .m-card h3{font-size:5.5px;margin:12px 0 5px}
.m-musicians .m-card .copy{font-size:5px;line-height:8px;padding:0 20px}
.m-musicians .m-card .btn{font-size:5.5px;padding:5px 10px}
.m-about{height:631px;padding:40px 14px 0}
.m-about h2.section{font-size:17px;text-align:right;margin-bottom:12px}
.m-about .text{text-align:center}
.m-about .btn{float:right}
.m-about .photo{height:322px;margin-top:22px;background:var(--clinic-tone)}
.m-location{height:139px;text-align:center;padding:0 14px}
.m-location h2.section{font-size:17px;margin-bottom:10px}
.m-location .loc{width:auto;font-size:6px;line-height:10px;border:0;margin-bottom:8px}
.m-location .loc strong{text-decoration:underline;font-size:6.5px}
.m-map{height:162px;background:var(--map-tone)}
.m-footer{height:617px;background:var(--dark);color:#ccc;font-size:6px;padding:30px 14px 0}
.m-footer h4{font:700 6.5px var(--sans);color:var(--white);text-transform:uppercase;margin-bottom:12px}
.m-footer .block{height:106px}
.m-footer li{display:flex;gap:6px;align-items:center;margin-bottom:9px}
.m-footer .ico{width:11px;height:11px}
.m-footer .subscribe{width:150px;height:18px}
.m-footer .links{width:100%;column-gap:20px;row-gap:4px}
.m-footer .copyright{position:static;padding-top:12px;font-size:5.5px}
</style>
</head>
<body>

<main class="desktop">
  <div class="topbar">
    <span><svg width="8" height="8" viewBox="0 0 10 10"><path d="M2 1l2 2-1 1.5c.7 1.3 1.5 2 2.5 2.5L7 6l2 2-1.3 1.3C4.5 9 1 5.5.7 2.3z" fill="#ddd"/></svg>Phone : (02) 9000 4417</span>
    <span><svg width="9" height="7" viewBox="0 0 10 7"><rect x=".5" y=".5" width="9" height="6" fill="none" stroke="#ddd"/><path d="M.5.5l4.5 3.5L9.5.5" fill="none" stroke="#ddd"/></svg>Mail : info@pelmorahearing.com.au</span>
  </div>
  <nav class="mainnav">
    <div class="brand"><span class="brand-dot"></span>Pelmora Hearing</div>
    <div class="menu"><span class="active">Your Hearing</span><span>Hearing Aids</span><span>Musicians</span><span>Doctors Information</span><span>About Us</span><span>Products</span><span>Contact us</span></div>
  </nav>

  <section class="hero photo" role="img" aria-label="Audiologist fitting a hearing aid behind an older man's ear">
    <div class="hero-lines"><span>To Hear</span><span>To Listen</span><span>To Live</span></div>
    <span class="hero-arrow" style="left:24px"><svg width="14" height="14" viewBox="0 0 14 14"><path d="M8 4L5 7l3 3" fill="none" stroke="#333" stroke-width="1.4"/></svg></span>
    <span class="hero-arrow" style="right:24px"><svg width="14" height="14" viewBox="0 0 14 14"><path d="M6 4l3 3-3 3" fill="none" stroke="#333" stroke-width="1.4"/></svg></span>
    <div class="service-card">
      <h2>Pelmora Hearing's Diagnostic Services</h2>
      <span class="btn">Learn more</span>
    </div>
  </section>

  <section class="aids">
    <div class="aids-photo photo" role="img" aria-label="Clinic consulting room with audiology equipment"></div>
    <div class="aids-photo inset photo" role="img" aria-label="Audiologist examining a patient's ear"></div>
    <div class="aids-copy">
      <h2 class="section">Hearing Aids</h2>
      <p class="copy">When considering a hearing aid it is important that you understand your hearing loss and your expectations of a hearing aid. There may be several hearing aids that are appropriate to your hearing loss, but there may only be one or two that comfortably fit the shape of your ear and successfully fit in with your life style. Many good hearing aids have automatic features such as a directional microphone and volume control. Digital hearing aids have become interfaces for telephones, music players and other devices, while also continuing to improve the tailored sound, speech clarity and your comfort. It is important when you are fitted with a hearing aid to work closely with your Audiologist to achieve your personally tailored amplification results.</p>
      <span class="btn">Learn more</span>
    </div>
  </section>

  <section class="musicians">
    <h2 class="section">Musicians</h2>
    <span class="side-arrow" style="left:62px"><svg width="18" height="18" viewBox="0 0 18 18"><path d="M10 6L7 9l3 3" fill="none" stroke="#333" stroke-width="1.3"/></svg></span>
    <article class="m-card" style="left:122px">
      <div class="photo" role="img" aria-label="Clear custom in-ear monitors on a dark surface" style="background:var(--iem-clear)"></div>
      <span class="tag"><svg width="12" height="12" viewBox="0 0 12 12"><path d="M8 1v6.5a2 2 0 1 1-1-1.7V1h3v2H8" fill="#fff"/></svg></span>
      <h3>Pelmora Hearing are resellers for Arvelle and Tessmond</h3>
      <p class="copy">Our Audiologists can take professional ear impressions for your custom fit In Ear Monitors. So if you are a range of IEM's.</p>
      <span class="btn">Learn more</span>
    </article>
    <article class="m-card" style="left:437px">
      <div class="photo" role="img" aria-label="Pair of blue custom in-ear monitors" style="background:var(--iem-blue)"></div>
      <span class="tag"><svg width="12" height="12" viewBox="0 0 12 12"><path d="M8 1v6.5a2 2 0 1 1-1-1.7V1h3v2H8" fill="#fff"/></svg></span>
      <h3>Pelmora Hearing are resellers for Arvelle and Tessmond</h3>
      <p class="copy">Our Audiologists can take professional ear impressions for your custom fit In Ear Monitors. So if you are a range of IEM's.</p>
      <span class="btn">Learn more</span>
    </article>
    <span class="side-arrow" style="right:62px"><svg width="18" height="18" viewBox="0 0 18 18"><path d="M8 6l3 3-3 3" fill="none" stroke="#333" stroke-width="1.3"/></svg></span>
  </section>

  <section class="about">
    <h2 class="section">About Us</h2>
    <p class="copy">Pelmora Hearing is an independently owned and managed professional audiology clinic. Our Audiologists are health care professionals specialising in diagnosing, treating and monitoring everything to do with hearing and balance. At Pelmora Hearing we work closely with Ear, Nose and Throat specialists to ensure you receive the highest standards of medical care.<br>Pelmora Hearing are state of the art hearing and balance clinics. We provide all brands of digital hearing aids, cochlear implants and assisted listening devices. We are diagnostic clinics offering hearing tests for adults and children, balance tests, tinnitus testing and treatment, and auditory processing tests.</p>
    <span class="btn">Learn more</span>
    <div class="about-photo photo" role="img" aria-label="Audiologist at a testing console with a patient in the booth"></div>
  </section>

  <section class="location">
    <h2 class="section">Our Location</h2>
    <div class="locs">
      <div class="loc"><strong>Kellbridge</strong>Ground Floor, Suite 4, 210 Harbour Road<br>Kellbridge, NSW, 2071</div>
      <div class="loc"><strong>Ashcombe</strong>Shop 2, 48 Marlow Street<br>Ashcombe, NSW, 2049</div>
    </div>
  </section>
  <div class="map photo" role="img" aria-label="Street map showing both clinic locations"></div>

  <footer class="footer">
    <div class="fcol" style="left:88px;top:42px">
      <h4>Social link</h4>
      <ul><li><span class="ico"></span>Community</li><li><span class="ico"></span>Email</li><li><span class="ico"></span>Network</li></ul>
    </div>
    <div class="fcol" style="left:270px;top:42px">
      <h4>Stay in touch</h4>
      <p>Subscribe to our Newsletter</p>
      <div class="subscribe">Email Address<svg width="10" height="10" viewBox="0 0 10 10"><path d="M0 5l10-5-3 10-2-4z" fill="#333"/></svg></div>
    </div>
    <div class="fcol" style="left:505px;top:42px">
      <h4>Information</h4>
      <ul>
        <li><span class="ico"></span>Call Us : (02) 9000 4417</li>
        <li><span class="ico"></span>Kellbridge Ground Floor, Suite 4, 210 Harbour Road<br>Kellbridge, NSW, 2071</li>
        <li><span class="ico"></span>info@pelmorahearing.com.au</li>
      </ul>
    </div>
    <div class="fcol" style="left:88px;top:178px">
      <h4>Navigation</h4>
      <div class="links"><span>Your Hearing</span><span>About Us</span><span>Hearing Aids</span><span>Products</span><span>Musicians</span><span>Contact us</span><span>Doctors Information</span><span>Privacy Policy</span></div>
    </div>
    <div class="fcol" style="left:440px;top:178px">
      <h4>Company</h4>
      <div class="links"><span>Support</span><span>Login</span><span>Customers</span><span>Terms and Condition</span><span>Help</span></div>
    </div>
    <p class="copyright">© Copyright 2018 pelmorahearing. All Rights Reserved.</p>
  </footer>
</main>

<main class="mobile">
  <div class="topbar"><span>Phone : (02) 9000 4417</span></div>
  <nav class="m-nav">
    <div class="brand"><span class="brand-dot"></span>Pelmora Hearing</div>
    <span class="toggle">MENU<svg width="10" height="8" viewBox="0 0 10 8"><path d="M0 1h10M0 4h10M0 7h10" stroke="#333" stroke-width="1.2"/></svg></span>
  </nav>
  <section class="m-hero photo" role="img" aria-label="Audiologist fitting a hearing aid behind an older man's ear">
    <div class="hero-lines"><span>To Hear</span><span>To Listen</span><span>To Live</span></div>
    <div class="service-card"><h2>Pelmora Hearing's Diagnostic Services</h2><span class="btn">Learn more</span></div>
  </section>
  <section class="m-aids">
    <div class="photo" role="img" aria-label="Audiologist examining a patient's ear in the clinic"></div>
    <h2 class="section">Hearing Aids</h2>
    <p class="copy">When considering a hearing aid it is important that you understand your hearing loss and your expectations of a hearing aid. There may be several hearing aids that are appropriate to your hearing loss, but there may only be one or two that comfortably fit the shape of your ear and successfully fit in with your life style. Many good hearing aids have automatic features such as a directional microphone and volume control. Digital hearing aids have become interfaces for telephones, music players and other devices, while also continuing to improve.</p>
    <span class="btn">Learn more</span>
  </section>
  <section class="m-musicians">
    <h2 class="section">Musicians</h2>
    <article class="m-card">
      <div class="photo" role="img" aria-label="Clear custom in-ear monitors on a dark surface" style="background:var(--iem-clear)"></div>
      <span class="tag"><svg width="10" height="10" viewBox="0 0 12 12"><path d="M8 1v6.5a2 2 0 1 1-1-1.7V1h3v2H8" fill="#fff"/></svg></span>
      <h3>Pelmora Hearing are resellers for Arvelle and Tessmond</h3>
      <p class="copy">Our Audiologists can take professional ear impressions for your custom fit In Ear Monitors. So if you are a range of IEM's.</p>
      <span class="btn">Learn more</span>
    </article>
    <article class="m-card" style="margin-bottom:0">
      <div class="photo" role="img" aria-label="Pair of blue custom in-ear monitors" style="background:var(--iem-blue)"></div>
      <span class="tag"><svg width="10" height="10" viewBox="0 0 12 12"><path d="M8 1v6.5a2 2 0 1 1-1-1.7V1h3v2H8" fill="#fff"/></svg></span>
      <h3>Pelmora Hearing are resellers for Arvelle and Tessmond</h3>
      <p class="copy">Our Audiologists can take professional ear impressions for your custom fit In Ear Monitors. So if you are a range of IEM's.</p>
      <span class="btn">Learn more</span>
    </article>
  </section>
  <section class="m-about">
    <h2 class="section">About Us</h2>
    <div class="text">
      <p class="copy">Pelmora Hearing is an independently owned and managed professional audiology clinic. Our Audiologists are health care professionals specialising in diagnosing, treating and monitoring everything to do with hearing and balance. At Pelmora Hearing we work closely with Ear, Nose and Throat specialists to ensure you receive the highest standards of medical care. Pelmora Hearing are state of the art hearing and balance clinics. We provide all brands of digital hearing aids, cochlear implants and assisted listening devices. We are diagnostic clinics.</p>
      <span class="btn">Learn more</span>
    </div>
    <div style="clear:both"></div>
    <div class="photo" role="img" aria-label="Audiologist at a testing console with a patient in the booth"></div>
  </section>
  <section class="m-location">
    <h2 class="section">Our Location</h2>
    <div class="loc"><strong>Kellbridge</strong>Ground Floor, Suite 4, 210 Harbour Road<br>Kellbridge, NSW, 2071</div>
    <div class="loc"><strong>Ashcombe</strong>Shop 2, 48 Marlow Street<br>Ashcombe, NSW, 2049</div>
  </section>
  <div class="m-map photo" role="img" aria-label="Street map showing both clinic locations"></div>
  <footer class="m-footer">
    <div class="block"><h4>Social link</h4><ul><li><span class="ico"></span>Community</li><li><span class="ico"></span>Email</li><li><span class="ico"></span>Network</li></ul></div>
    <div class="block"><h4>Stay in touch</h4><p>Subscribe to our Newsletter</p><div class="subscribe">Email Address<svg width="9" height="9" viewBox="0 0 10 10"><path d="M0 5l10-5-3 10-2-4z" fill="#333"/></svg></div></div>
    <div class="block"><h4>Information</h4><ul><li><span class="ico"></span>Call Us : (02) 9000 4417</li><li><span class="ico"></span>Kellbridge Ground Floor, Suite 4, 210 Harbour Road<br>Kellbridge, NSW, 2071</li><li><span class="ico"></span>info@pelmorahearing.com.au</li></ul></div>
    <div class="block"><h4>Navigation</h4><div class="links"><span>Your Hearing</span><span>About Us</span><span>Hearing Aids</span><span>Products</span><span>Musicians</span><span>Contact us</span><span>Doctors Information</span><span>Privacy Policy</span></div></div>
    <div class="block"><h4>Company</h4><div class="links"><span>Support</span><span>Login</span><span>Customers</span><span>Terms and Condition</span><span>Help</span></div></div>
    <p class="copyright">© Copyright 2018 pelmorahearing. All Rights Reserved.</p>
  </footer>
</main>

</body>
</html>
```